CRPG is needing business cards, and stationary created.

Pixel Forge created a logo for our business, and now we are wanting business cards, and stationary. I have included two designs of the same logo. Please feel free to use them as you want. The name of the company is Cedar Ridge Property Group LLC, the address is 812 NE Willow Ln., Suite 9, the city & state is Bend, Oregon, zip code is 97815, Telephone number is 541-327-4489, Fax number is 541-327-6051, the name on the business card is Carl Whitby CMCA

Industry/Entity Type

Property Management

Contact Information for Business Card

The card needs to look professional. Upscale.

Requirements
Must have
• The colors we are using are on the logo that has been uploaded.

```html
<!DOCTYPE html>
<html lang="en">
<head>
<meta charset="utf-8">
<title>Cedar Ridge Property Group – Business Card</title>
<link href="https://fonts.googleapis.com/css2?family=Exo+2:wght@500;600&family=Open+Sans:wght@400;600&display=swap" rel="stylesheet">
<style>
  :root {
    --backdrop: #5b5b5d;
    --teal: #178f7a;
    --slate: #3b4757;
    --white: #ffffff;
    --shadow: rgba(0,0,0,0.45);
  }
  * { margin: 0; padding: 0; box-sizing: border-box; }
  html, body { width: 1200px; height: 802px; overflow: hidden; }
  body { background: var(--backdrop); position: relative; font-family: "Open Sans", sans-serif; }

  .card {
    position: absolute; top: 274px; width: 442px; height: 264px;
    box-shadow: 2px 3px 6px var(--shadow); overflow: hidden;
  }
  .card--front { left: 136px; background: var(--teal); }
  .card--back  { left: 624px; background: var(--white); }

  /* front */
  .front__panel {
    position: absolute; left: 0; top: 0; width: 190px; height: 100%;
    background: var(--slate);
    display: flex; align-items: center; justify-content: center;
  }
  .front__initials {
    font-family: "Exo 2", sans-serif; font-weight: 600; font-size: 46px;
    color: var(--teal); letter-spacing: 2px;
  }
  .front__details {
    position: absolute; right: 26px; top: 94px; text-align: right; color: var(--white);
  }
  .holder-name {
    font-family: "Exo 2", sans-serif; font-weight: 500; font-size: 16px; letter-spacing: 0.2px;
  }
  .holder-name .credential { font-size: 12px; }
  .contact-lines { margin-top: 12px; font-size: 13px; line-height: 15.5px; }
  .contact-line { display: flex; justify-content: flex-end; align-items: center; gap: 4px; }
  .contact-line svg { width: 11px; height: 11px; fill: var(--white); }
  .address { margin-top: 8px; font-size: 13px; line-height: 16px; }

  /* back */
  .brand {
    position: absolute; left: 0; right: 0; top: 0; bottom: 0;
    display: flex; flex-direction: column; align-items: center; justify-content: center;
    gap: 14px;
  }
  .brand__mark {
    width: 30px; height: 30px; background: var(--slate);
  }
  .brand__name {
    font-family: "Exo 2", sans-serif; font-weight: 600; font-size: 22px; line-height: 26px;
    color: var(--teal); letter-spacing: 0.5px;
  }
</style>
</head>
<body>
  <section class="card card--front" aria-label="Business card front">
    <div class="front__panel"><span class="front__initials">CRPG</span></div>
    <div class="front__details">
      <p class="holder-name">CARL WHITBY <span class="credential">CMCA</span></p>
      <div class="contact-lines">
        <p class="contact-line">541-327-4489
          <svg viewBox="0 0 24 24" aria-hidden="true"><path d="M3 9c0-3 4-5 9-5s9 2 9 5v2h-5V9H8v2H3z M6 12h12l2 8H4z"/></svg>
        </p>
        <p class="contact-line">541-327-6051
          <svg viewBox="0 0 24 24" aria-hidden="true"><path d="M7 2h10v6H7z M3 9h18v9h-4v-4H7v4H3z M8 15h8v7H8z"/></svg>
        </p>
      </div>
      <p class="address">812 NE Willow Ln., Suite 9<br>Bend, Oregon, 97815</p>
    </div>
  </section>

  <section class="card card--back" aria-label="Business card back">
    <div class="brand">
      <div class="brand__mark"></div>
      <p class="brand__name">Cedar Ridge Property Group</p>
    </div>
  </section>
</body>
</html>
```